Non-Profit, Organic, Natural Feel, Clean & Simple Business Cards

Looking for a business card design. Has an organic, natural, new-age, clean and simple look/feel. We are a non-profit group that works with Moringa(a health plant/superfood) by spreading and sharing seeds of Moringa. A design that stands out but clean and professional. I will upload our new logo design. The font can be changed. Also I will upload some pictures of Moringa.
Our Facebook page is www.socialvine.com/TavelliCircle Check us out to get a feel of us.

Target Market(s)

Everyone. Movers & Shakers of The Sustainable, Natural Medicines & Cosmetics, Organic Food Farming Industry. And To The Common Person Or A Local Family.

Industry/Entity Type

Sustainability

Contact Information for Business Card

Email: TavelliSoilCircle@Postvane.com
FB: www.Socialvine.com/TavelliCircle
Website: www.TavelliCircle.com

Requirements
Must have
• Image/Pic/Design of Moringa Leaves. Somewhere on the card. Clean and Clear. So you could easily identify the Moringa from the Business Card. Something Alive, Living, Green Feel to the card design.
Nice to have
• A warm, friendly, professional feel to the design. A organic sustainable concept/future with Moringa is the business card impression/image we are trying to present.

```html
<!DOCTYPE html>
<html lang="en">
<head>
<meta charset="utf-8">
<title>Tavelli Circle – Business Cards</title>
<link rel="stylesheet" href="https://fonts.googleapis.com/css2?family=Open+Sans:wght@400;600;700&display=swap">
<style>
  :root {
    --backdrop: #e9e7e2;
    --card-white: #ffffff;
    --card-grey: #8e8f83;
    --leaf-green: #5cb83a;
    --leaf-green-light: #7cd05a;
    --ink-grey: #6f706a;
    --ink-dark: #3a3b37;
    --swoosh-grey: #b8b9b2;
    --rule: #2f302c;
  }
  * { margin: 0; padding: 0; box-sizing: border-box; }
  html, body { width: 1200px; height: 950px; overflow: hidden; }
  body {
    background: var(--backdrop);
    font-family: "Open Sans", Arial, sans-serif;
    position: relative;
  }
  .card {
    position: absolute;
    left: 250px;
    width: 700px;
    height: 400px;
    overflow: hidden;
    box-shadow: 0 6px 18px rgba(0,0,0,0.18);
  }
  .card--back { top: 50px; background: var(--card-grey); }
  .card--front { top: 500px; background: var(--card-white); }

  /* Back */
  .brand {
    position: absolute;
    display: flex;
    align-items: center;
    gap: 16px;
  }
  .brand__mark { width: 46px; height: 46px; border: 4px solid currentColor; }
  .brand__name {
    font-weight: 600;
    font-size: 40px;
    letter-spacing: 3px;
    text-transform: uppercase;
    line-height: 1;
  }
  .card--back .brand { left: 50%; top: 150px; transform: translateX(-50%); color: #fff; }
  .card--back .site {
    position: absolute;
    left: 0; right: 0;
    top: 270px;
    text-align: center;
    color: #fff;
    font-size: 17px;
    letter-spacing: 2px;
  }

  /* Front */
  .card--front .brand { left: 240px; top: 62px; color: var(--ink-grey); }
  .card--front .brand__mark { border-color: var(--leaf-green); }
  .card--front .brand__name { font-size: 36px; }
  .logo-rule {
    position: absolute; left: 240px; top: 135px;
    width: 400px; height: 2px; background: var(--rule);
  }
  .social {
    position: absolute; right: 60px; top: 205px;
    display: flex; align-items: center; gap: 8px;
    font-size: 16px; color: var(--ink-dark);
  }
  .social__square { width: 14px; height: 14px; background: var(--leaf-green); }
  .person { position: absolute; left: 150px; top: 238px; }
  .person__name { color: var(--leaf-green); font-weight: 700; font-size: 24px; }
  .person__role { color: #9a9b94; font-size: 17px; }
  .name-rule {
    position: absolute; left: 290px; top: 262px;
    width: 330px; height: 2px; background: var(--rule);
  }
  .contacts {
    position: absolute; left: 150px; top: 308px;
    list-style: none; font-size: 16px; color: var(--ink-dark);
  }
  .contacts li { display: flex; align-items: center; gap: 12px; height: 26px; }
  .contacts svg { width: 16px; height: 16px; flex: none; }
  .swoosh { position: absolute; inset: 0; width: 700px; height: 400px; }
</style>
</head>
<body>

<section class="card card--back" aria-label="Card back">
  <div class="brand">
    <span class="brand__mark"></span>
    <span class="brand__name">Tavelli Circle</span>
  </div>
  <p class="site">www.TavelliCircle.com</p>
</section>

<section class="card card--front" aria-label="Card front">
  <svg class="swoosh" viewBox="0 0 700 400" aria-hidden="true">
    <path d="M0 400 L0 385 C180 400 330 340 450 280 C540 238 620 215 700 212 L700 400 Z" fill="var(--swoosh-grey)"/>
    <path d="M0 400 L0 395 C200 410 350 360 470 305 C560 262 630 240 700 236 L700 400 Z" fill="var(--leaf-green)"/>
    <path d="M0 400 C220 405 380 370 500 322 C580 290 640 272 700 268 L700 400 Z" fill="var(--leaf-green-light)" opacity="0.55"/>
  </svg>

  <div class="brand">
    <span class="brand__mark"></span>
    <span class="brand__name">Tavelli Circle</span>
  </div>
  <div class="logo-rule"></div>

  <div class="social">
    <span class="social__square"></span>
    <span>/TavelliCircle</span>
  </div>

  <div class="person">
    <p class="person__name">Maren Holt</p>
    <p class="person__role">President</p>
  </div>
  <div class="name-rule"></div>

  <ul class="contacts">
    <li>
      <svg viewBox="0 0 16 16"><rect x="1" y="3" width="14" height="10" rx="1" fill="var(--leaf-green)"/><path d="M1.5 3.5 L8 9 L14.5 3.5" stroke="#fff" stroke-width="1.4" fill="none"/></svg>
      <span>TavelliSoilCircle@Postvane.com</span>
    </li>
    <li>
      <svg viewBox="0 0 16 16"><circle cx="8" cy="8" r="7" fill="var(--leaf-green)"/><ellipse cx="8" cy="8" rx="3" ry="6" stroke="#fff" stroke-width="1.1" fill="none"/><path d="M2 8 H14" stroke="#fff" stroke-width="1.1"/></svg>
      <span>www.TavelliCircle.com</span>
    </li>
  </ul>
</section>

</body>
</html>
```